Intranet for company management ERP Style

We need a redesign for our Intranet webpage (Images, CSS), we have all the code and functionality ready and a basic design but it is not good looking. In order to meet our company standards this design has to be fully responsive and elegant, also should display the colors of the company: (#F17808 #EDAA64 #F4B947 #F2A900 #292828 #3D3D3D #062953) usually Dark orange colors are the main ones, though we wouldn't mind to see other options or to implement a pair of skins that we could switch easily on the webpage.
Access to the webpage can be granted

Target Market(s)

this webpage is for internal use of the company but could also be sold to external customers in the future, our market is cryptocurrency and BPO

Industry/Entity Type

BPO, Cryptocurrency

Coding

Coded - Design and coding required

Number of Pages Required

1 page

Font styles to use
Other font styles liked:
• Headings: Montserrat Extra Bold, Sub headings: Montserrat, Text: Object Sans

Colors
F0912C
F2A743
F7CA91
FBE8D2
FDF5EE

Requirements
Nice to have
• elegant icons designs and menus

```html
<!DOCTYPE html>
<html lang="en">
<head>
<meta charset="utf-8">
<title>Northgate Desk – Suggestion</title>
<link href="https://fonts.googleapis.com/css2?family=Montserrat:wght@400;500;600;700;800&display=swap" rel="stylesheet">
<style>
:root{
  --orange-dark:#e8751c;
  --orange:#f0912c;
  --orange-mid:#f2a743;
  --peach:#f7ca91;
  --sand:#fbe8d2;
  --cream:#fdf5ee;
  --ink:#292828;
  --ink-soft:#3d3d3d;
  --footer:#1e1e1e;
  --line:#d9d2cb;
  --stage:#4a4a4a;
}
*{box-sizing:border-box;margin:0;padding:0}
html,body{width:795px;height:1200px;overflow:hidden}
body{background:radial-gradient(ellipse at center,#5c5c5c 0%,#3a3a3a 60%,#2d2d2d 100%);font-family:"Montserrat",sans-serif;color:var(--ink);position:relative}
.screen{position:absolute;left:39px;width:716px;height:553px;background:var(--cream);box-shadow:0 6px 24px rgba(0,0,0,.45);overflow:hidden}
.screen--form{top:35px}
.screen--list{top:613px}

.brand{position:absolute;left:0;top:0;width:122px;height:42px;background:linear-gradient(90deg,var(--orange-mid),var(--orange));display:flex;align-items:center;justify-content:center;gap:5px}
.brand-dot{width:9px;height:9px;border-radius:50%;background:#fff}
.brand-name{color:#fff;font-weight:700;font-size:10px;letter-spacing:.2px}

.topbar{position:absolute;left:122px;top:0;right:0;height:42px;background:#fff;border-bottom:1px solid #bcb6b0}
.tool{position:absolute;top:10px;width:24px;height:23px;border:1px solid #cfcac5;background:#fff;display:flex;align-items:center;justify-content:center}
.tool svg{width:10px;height:10px}
.badge{position:absolute;top:-5px;right:-4px;width:7px;height:7px;border-radius:50%;background:#fff;border:1.2px solid var(--orange);font-size:4.5px;color:var(--orange);font-weight:700;display:flex;align-items:center;justify-content:center}

.sidebar{position:absolute;left:0;top:42px;width:122px;bottom:46px;background:linear-gradient(180deg,#faead8,#f9e3cc);border-right:1px solid #e0cdb8}
.nav-item{position:absolute;left:0;width:122px;height:24px;display:flex;align-items:center;font-size:7.2px;font-weight:500;color:var(--ink)}
.nav-item svg{position:absolute;left:6px;width:7px;height:7px}
.nav-item span{position:absolute;left:21px}
.nav-item .chev{position:absolute;right:7px;font-size:8px;font-weight:700;left:auto}
.nav-item--active{background:linear-gradient(90deg,var(--orange-mid),var(--orange-dark));color:#fff}
.nav-item--accent{color:var(--orange)}
.quick{position:absolute;top:410px;width:40px;text-align:center;font-size:6px;font-weight:500;line-height:7px}
.quick svg{width:9px;height:9px;display:block;margin:0 auto 3px}

.footer{position:absolute;left:0;right:0;bottom:0;height:46px;background:var(--footer);color:#e9e9e9;font-size:7.8px;display:flex;align-items:center;justify-content:center}

.page-title{position:absolute;left:142px;top:64px;font-size:15.5px;font-weight:800;color:var(--ink);letter-spacing:.2px}
.crumbs{position:absolute;left:142px;top:95px;font-size:8px;color:var(--ink-soft)}
.crumbs a{color:var(--orange);text-decoration:none}
.counter{position:absolute;right:31px;top:67px;font-size:8px;color:var(--ink-soft)}

.card{position:absolute;left:142px;width:556px;background:#fff;box-shadow:0 2px 10px rgba(0,0,0,.07)}
.card--form{top:124px;height:360px}
.card--list{top:129px;height:355px}
.card-head{height:23px;background:linear-gradient(90deg,#f5ac4e 0%,#f2a743 50%,var(--orange-dark) 55%,var(--orange-dark) 100%);color:#fff;font-weight:800;font-size:10.5px;display:flex;align-items:center;padding-left:19px}
.field-label{position:absolute;left:27px;font-size:8.6px;color:var(--ink)}
.field-box{position:absolute;left:212px;width:318px;height:59px;border:1px solid #cfcac5;border-radius:3px}
.field-select{height:27px;display:flex;align-items:center;padding-left:15px;font-size:8px;color:var(--ink-soft)}
.field-select::after{content:"";position:absolute;right:14px;top:12px;border-left:3px solid transparent;border-right:3px solid transparent;border-top:3px solid var(--ink)}
.btn-save{position:absolute;left:185px;top:305px;width:86px;height:33px;border-radius:17px;background:linear-gradient(90deg,var(--orange),var(--orange-mid));color:#fff;font-weight:800;font-size:11px;display:flex;align-items:center;justify-content:center}

.exports{position:absolute;left:16px;top:21px;display:flex;gap:2px}
.exports span{width:49px;height:23px;border-radius:12px;background:#ece9e6;font-size:8.5px;font-weight:500;display:flex;align-items:center;justify-content:center}
.search{position:absolute;left:438px;top:21px;width:104px;height:24px;border:1px solid #bdb7b2;border-radius:12px;font-size:6.8px;display:flex;align-items:center;padding-left:11px;color:var(--ink-soft)}
.search svg{position:absolute;right:7px;width:9px;height:9px}

.grid{position:absolute;left:9px;top:59px;width:538px;border-collapse:collapse;font-size:6.8px}
.grid th{height:22px;background:linear-gradient(90deg,var(--orange-mid),var(--orange-dark));color:#fff;font-weight:700;text-align:left;font-size:6.8px}
.grid td{height:22.6px;border-bottom:1px solid #d6d0ca;color:var(--ink)}
.grid tr:nth-child(even) td{background:#f2eeeb}
.grid .c1{width:98px;padding-left:12px}
.grid th.c1{padding-left:12px}
.grid .c2{width:114px}.grid .c3{width:125px}.grid .c4{width:99px}
.sort{font-size:5px;margin-left:4px}
.summary{position:absolute;left:21px;top:245px;font-size:8px;font-weight:500}
.pager{position:absolute;left:369px;top:238px;width:160px;height:25px;border:1px solid #bdb7b2;border-radius:13px;font-size:8px;display:flex;align-items:center}
.pager .prev{position:absolute;left:13px}
.pager .current{position:absolute;left:67px;top:-1px;width:25px;height:25px;border-radius:50%;background:var(--orange);color:#fff;font-weight:700;display:flex;align-items:center;justify-content:center}
.pager .next{position:absolute;right:17px}
.gear-fab{position:absolute;left:490px;top:345px;width:19px;height:19px;border-radius:50%;background:var(--orange);display:flex;align-items:center;justify-content:center}
</style>
</head>
<body>

<!-- Screen: add suggestion form -->
<section class="screen screen--form">
  <div class="brand"><span class="brand-dot"></span><span class="brand-name">Northgate Desk</span></div>
  <header class="topbar">
    <div class="tool" style="left:13px"><svg viewBox="0 0 10 10"><path d="M1 2h8M1 5h8M1 8h8" stroke="#f0912c" stroke-width="1.4"/></svg></div>
    <div class="tool" style="left:42px"><svg viewBox="0 0 10 10"><circle cx="4.2" cy="4.2" r="3" fill="none" stroke="#f0912c" stroke-width="1.4"/><path d="M6.5 6.5L9 9" stroke="#f0912c" stroke-width="1.5"/></svg></div>
    <div class="tool" style="left:70px"><svg viewBox="0 0 10 10" fill="#f0912c"><rect x="0.5" y="0.5" width="4" height="4"/><rect x="5.5" y="0.5" width="4" height="4"/><rect x="0.5" y="5.5" width="4" height="4"/><rect x="5.5" y="5.5" width="4" height="4"/></svg></div>
    <div class="tool" style="left:529px"><svg viewBox="0 0 10 10"><rect x="0.5" y="2" width="9" height="6.5" fill="#292828"/><path d="M0.5 2L5 5.5L9.5 2" stroke="#fff" stroke-width=".8" fill="none"/></svg><span class="badge">0</span></div>
    <div class="tool" style="left:558px"><svg viewBox="0 0 10 10" fill="#292828"><circle cx="5" cy="3" r="2.2"/><path d="M1 9.5c0-3 1.8-4 4-4s4 1 4 4z"/></svg></div>
  </header>

  <nav class="sidebar">
    <div class="nav-item" style="top:14px"><svg viewBox="0 0 8 8"><circle cx="4" cy="4" r="3.5" fill="#f0912c"/></svg><span>Home</span></div>
    <div class="nav-item" style="top:40px"><svg viewBox="0 0 8 8"><rect x=".5" y=".5" width="7" height="7" fill="none" stroke="#f0912c"/><path d="M2 4l1.5 1.5L6.5 2" stroke="#f0912c" fill="none"/></svg><span>Requests</span></div>
    <div class="nav-item" style="top:66px"><svg viewBox="0 0 8 8" fill="#f0912c"><rect x="1" y="3" width="1.2" height="5"/><rect x="3.3" y="1" width="1.2" height="7"/><rect x="5.6" y="4" width="1.2" height="4"/></svg><span>Reports</span></div>
    <div class="nav-item" style="top:92px"><span>Policy</span><span class="chev">»</span></div>
    <div class="nav-item" style="top:118px"><span>Suggestion Dashboard</span><span class="chev">»</span></div>
    <div class="nav-item" style="top:144px"><svg viewBox="0 0 8 8" fill="#f0912c"><circle cx="2" cy="4" r="1.5"/><circle cx="6" cy="1.8" r="1.5"/><circle cx="6" cy="6.2" r="1.5"/><path d="M2 4L6 1.8M2 4L6 6.2" stroke="#f0912c"/></svg><span>Helpdesk</span></div>
    <div class="nav-item" style="top:170px"><svg viewBox="0 0 8 8"><circle cx="4" cy="4" r="3.5" fill="#f0912c"/><path d="M2.5 4h3M4 2.5v3" stroke="#fff"/></svg><span>Payroll</span></div>
    <div class="nav-item nav-item--active" style="top:190px"><svg viewBox="0 0 8 8"><path d="M1.5 4a2.5 2.5 0 0 1 4.5-1.5M6.5 4a2.5 2.5 0 0 1-4.5 1.5" stroke="#fff" fill="none" stroke-width="1.2"/></svg><span>Suggestion Box</span></div>
    <div class="nav-item" style="top:216px"><svg viewBox="0 0 8 8"><path d="M4 .5L7 1.5v3C7 6 5.5 7.2 4 7.7 2.5 7.2 1 6 1 4.5v-3z" fill="#f0912c"/></svg><span>Administrator</span></div>
    <div class="quick" style="left:-4px"><svg viewBox="0 0 10 10"><circle cx="5" cy="5" r="4" fill="#f0912c"/><circle cx="5" cy="5" r="1.6" fill="#faead8"/></svg>Local<br>Host</div>
    <div class="quick" style="left:32px"><svg viewBox="0 0 10 10" fill="#f0912c"><rect x="1.5" y="4.5" width="7" height="5"/><path d="M3 4.5V3a2 2 0 0 1 4 0" stroke="#f0912c" fill="none" stroke-width="1.2"/></svg>Super<br>login</div>
    <div class="quick" style="left:76px"><svg viewBox="0 0 10 10" fill="#f0912c"><circle cx="5" cy="3" r="2.2"/><path d="M1 9.5c0-3 1.8-4 4-4s4 1 4 4z"/></svg>Admin<br>Dashboard</div>
  </nav>

  <h1 class="page-title">SUGGESTION</h1>
  <p class="crumbs"><a>HOME</a>&nbsp; &gt; &nbsp;ADD NEW SUGGESTION</p>

  <div class="card card--form">
    <div class="card-head">ADD NEW SUGGESTION</div>
    <label class="field-label" style="top:49px">Describe your Suggestion &nbsp;*</label>
    <div class="field-box" style="top:50px"></div>
    <label class="field-label" style="top:116px">How would you Suggestion Help Us ?</label>
    <div class="field-box" style="top:117px"></div>
    <label class="field-label" style="top:183px">Aditional Comment</label>
    <div class="field-box" style="top:185px"></div>
    <label class="field-label" style="top:251px">Country</label>
    <div class="field-box field-select" style="top:252px">Select</div>
    <div class="btn-save">SAVE</div>
  </div>

  <footer class="footer">© 2022 Northgate Desk. All rights reserved &nbsp;| &nbsp;Privacy &nbsp;| &nbsp;Terms of Use</footer>
</section>

<!-- Screen: suggestion report -->
<section class="screen screen--list">
  <div class="brand"><span class="brand-dot"></span><span class="brand-name">Northgate Desk</span></div>
  <header class="topbar">
    <div class="tool" style="left:13px"><svg viewBox="0 0 10 10"><path d="M1 2h8M1 5h8M1 8h8" stroke="#f0912c" stroke-width="1.4"/></svg></div>
    <div class="tool" style="left:42px"><svg viewBox="0 0 10 10"><circle cx="4.2" cy="4.2" r="3" fill="none" stroke="#f0912c" stroke-width="1.4"/><path d="M6.5 6.5L9 9" stroke="#f0912c" stroke-width="1.5"/></svg></div>
    <div class="tool" style="left:70px"><svg viewBox="0 0 10 10" fill="#f0912c"><rect x="0.5" y="0.5" width="4" height="4"/><rect x="5.5" y="0.5" width="4" height="4"/><rect x="0.5" y="5.5" width="4" height="4"/><rect x="5.5" y="5.5" width="4" height="4"/></svg></div>
    <div class="tool" style="left:529px"><svg viewBox="0 0 10 10"><rect x="0.5" y="2" width="9" height="6.5" fill="#292828"/><path d="M0.5 2L5 5.5L9.5 2" stroke="#fff" stroke-width=".8" fill="none"/></svg><span class="badge">0</span></div>
    <div class="tool" style="left:558px"><svg viewBox="0 0 10 10" fill="#292828"><circle cx="5" cy="3" r="2.2"/><path d="M1 9.5c0-3 1.8-4 4-4s4 1 4 4z"/></svg></div>
  </header>

  <nav class="sidebar">
    <div class="nav-item" style="top:14px"><svg viewBox="0 0 8 8"><circle cx="4" cy="4" r="3.5" fill="#f0912c"/></svg><span>Home</span></div>
    <div class="nav-item" style="top:40px"><svg viewBox="0 0 8 8"><rect x=".5" y=".5" width="7" height="7" fill="none" stroke="#f0912c"/><path d="M2 4l1.5 1.5L6.5 2" stroke="#f0912c" fill="none"/></svg><span>Requests</span></div>
    <div class="nav-item nav-item--active" style="top:60px"><svg viewBox="0 0 8 8" fill="#fff"><rect x="1" y="3" width="1.2" height="5"/><rect x="3.3" y="1" width="1.2" height="7"/><rect x="5.6" y="4" width="1.2" height="4"/></svg><span>Reports</span></div>
    <div class="nav-item" style="top:92px"><span>Policy</span><span class="chev">»</span></div>
    <div class="nav-item nav-item--accent" style="top:118px"><span>Suggestion Dashboard</span><span class="chev">»</span></div>
    <div class="nav-item" style="top:144px"><svg viewBox="0 0 8 8" fill="#f0912c"><circle cx="2" cy="4" r="1.5"/><circle cx="6" cy="1.8" r="1.5"/><circle cx="6" cy="6.2" r="1.5"/><path d="M2 4L6 1.8M2 4L6 6.2" stroke="#f0912c"/></svg><span>Helpdesk</span></div>
    <div class="nav-item" style="top:170px"><svg viewBox="0 0 8 8"><circle cx="4" cy="4" r="3.5" fill="#f0912c"/><path d="M2.5 4h3M4 2.5v3" stroke="#fff"/></svg><span>Payroll</span></div>
    <div class="nav-item" style="top:196px"><svg viewBox="0 0 8 8"><path d="M1.5 4a2.5 2.5 0 0 1 4.5-1.5M6.5 4a2.5 2.5 0 0 1-4.5 1.5" stroke="#f0912c" fill="none" stroke-width="1.2"/></svg><span>Suggestion Box</span></div>
    <div class="nav-item" style="top:222px"><svg viewBox="0 0 8 8"><path d="M4 .5L7 1.5v3C7 6 5.5 7.2 4 7.7 2.5 7.2 1 6 1 4.5v-3z" fill="#f0912c"/></svg><span>Administrator</span></div>
    <div class="quick" style="left:-4px"><svg viewBox="0 0 10 10"><circle cx="5" cy="5" r="4" fill="#f0912c"/><circle cx="5" cy="5" r="1.6" fill="#faead8"/></svg>Local<br>Host</div>
    <div class="quick" style="left:32px"><svg viewBox="0 0 10 10" fill="#f0912c"><rect x="1.5" y="4.5" width="7" height="5"/><path d="M3 4.5V3a2 2 0 0 1 4 0" stroke="#f0912c" fill="none" stroke-width="1.2"/></svg>Super<br>login</div>
    <div class="quick" style="left:76px"><svg viewBox="0 0 10 10" fill="#f0912c"><circle cx="5" cy="3" r="2.2"/><path d="M1 9.5c0-3 1.8-4 4-4s4 1 4 4z"/></svg>Admin<br>Dashboard</div>
  </nav>

  <h1 class="page-title">SUGGESTION</h1>
  <p class="counter">Suggestion Number 4</p>
  <p class="crumbs"><a>REPORTS</a>&nbsp; &gt; &nbsp;SUGGESTION</p>

  <div class="card card--list">
    <div class="exports"><span>Copy</span><span>CSV</span><span>EXCEL</span><span>PDF</span><span>PRINT</span></div>
    <div class="search">Search<svg viewBox="0 0 10 10"><circle cx="4.2" cy="4.2" r="3" fill="none" stroke="#f0912c" stroke-width="1.4"/><path d="M6.5 6.5L9 9" stroke="#f0912c" stroke-width="1.5"/></svg></div>
    <table class="grid">
      <thead><tr><th class="c1">USERNAME<span class="sort">▲</span></th><th class="c2">DESCRIPTION<span class="sort">◆</span></th><th class="c3">SUGGESTION HELP<span class="sort">◆</span></th><th class="c4">COMMENTS<span class="sort">◆</span></th><th>DATE<span class="sort">◆</span></th></tr></thead>
      <tbody>
        <tr><td class="c1">Super admin</td><td>hola</td><td>hola</td><td>test</td><td>25 Nov 2021 &nbsp;08:48 PM</td></tr>
        <tr><td class="c1">Super admin</td><td>hola</td><td>hola</td><td>hghgff</td><td>25 Nov 2021 &nbsp;08:48 PM</td></tr>
        <tr><td class="c1">Super admin</td><td>dgffsdfs</td><td>hola</td><td>ewee</td><td>25 Nov 2021 &nbsp;08:48 PM</td></tr>
        <tr><td class="c1">Super admin</td><td>qwervgvdvf</td><td>hola</td><td>wewewеqwe</td><td>25 Nov 2021 &nbsp;08:48 PM</td></tr>
        <tr><td class="c1">Super admin</td><td>hola</td><td>zswewqw</td><td>test</td><td>25 Nov 2021 &nbsp;08:48 PM</td></tr>
        <tr><td class="c1">Super admin</td><td>ferqwqw</td><td>hola</td><td>hdfdf</td><td>25 Nov 2021 &nbsp;08:48 PM</td></tr>
      </tbody>
    </table>
    <p class="summary">Showing 1 to 6 of 6 entries</p>
    <div class="pager"><span class="prev">Previous</span><span class="current">1</span><span class="next">Next</span></div>
    <div class="gear-fab"><svg viewBox="0 0 10 10" width="9" height="9"><circle cx="5" cy="5" r="3.6" fill="#fff"/><circle cx="5" cy="5" r="1.4" fill="#f0912c"/></svg></div>
  </div>

  <footer class="footer">© 2022 Northgate Desk. All rights reserved &nbsp;| &nbsp;Privacy &nbsp;| &nbsp;Terms of Use</footer>
</section>

</body>
</html>
```